Dental marketing ad poster

I recently opened a new dental practice about 2 months ago and would like to have an ad designed for an A-frame poster to place outside our office. The goal of this ad is to attract and appeal to potential patients so they feel encouraged to come into the practice.
I’m leaving the creative direction up to you—I’d like to see what you can come up with. The ad can be funny or serious, but it should be eye-catching and patient-focused. Please highlight that we provide crowns, implants and teeth whitening.
My theme color is green but I’ll accept any color
Let me see your ideas!
Dentistry

```html
<!DOCTYPE html>
<html lang="en">
<head>
<meta charset="UTF-8">
<title>Meadowfield Dentistry – A-Frame Poster</title>
<link href="https://fonts.googleapis.com/css2?family=Rubik:wght@600;700&family=Open+Sans:wght@400;500&display=swap" rel="stylesheet">
<style>
  :root {
    --page-bg: #f2f3f2;
    --green-deep: #12895a;
    --green-mid: #1a9a66;
    --green-light: #4fae88;
    --lime: #c6de3a;
    --ink-light: #f4f8f2;
  }
  * { box-sizing: border-box; margin: 0; padding: 0; }
  html, body {
    width: 1200px; height: 927px; overflow: hidden;
    background: var(--page-bg);
  }
  .poster {
    position: absolute; left: 340px; top: 22px;
    width: 520px; height: 883px; overflow: hidden;
    background:
      radial-gradient(ellipse at 95% 40%, rgba(120,200,160,0.55), transparent 55%),
      linear-gradient(180deg, var(--green-mid) 0%, var(--green-deep) 60%, var(--green-mid) 100%);
    color: var(--ink-light);
    font-family: "Open Sans", sans-serif;
  }
  .brand {
    position: absolute; top: 60px; left: 0; right: 0;
    text-align: center; color: var(--lime);
    font-family: "Rubik", sans-serif; font-weight: 600;
  }
  .brand-name { font-size: 56px; line-height: 1; letter-spacing: -0.5px; }
  .brand-sub { font-size: 25px; line-height: 1; letter-spacing: 6px; margin-top: 10px; }
  .hero-art {
    position: absolute; top: 185px; left: 60px; width: 400px; height: 250px;
    border-radius: 12px;
    background: radial-gradient(ellipse at 50% 45%, #e9eeec 0%, #cfd9d4 38%, rgba(26,154,102,0) 70%);
  }
  .services {
    position: absolute; top: 448px; left: 30px; right: 30px;
    display: grid; grid-template-columns: repeat(3, 1fr);
    row-gap: 14px; column-gap: 10px; text-align: center;
  }
  .service-icon { width: 44px; height: 46px; display: block; margin: 0 auto 4px; }
  .service-title {
    font-family: "Rubik", sans-serif; font-weight: 700;
    color: var(--lime); font-size: 21px; line-height: 1.12;
  }
  .service-text { font-size: 11.5px; line-height: 1.35; margin-top: 6px; padding: 0 4px; }
  .web {
    position: absolute; left: 40px; right: 40px; top: 815px;
    border-top: 2px solid var(--lime);
    border-bottom: 2px solid var(--lime);
    padding: 4px 0 6px; text-align: center;
    font-family: "Rubik", sans-serif; font-weight: 700;
    color: var(--lime); font-size: 22px; line-height: 1.1; letter-spacing: 0.8px;
  }
</style>
</head>
<body>
  <main class="poster">
    <header class="brand">
      <div class="brand-name">Meadowfield</div>
      <div class="brand-sub">DENTISTRY</div>
    </header>

    <div class="hero-art" role="img" aria-label="Illustration of two friendly white cartoon teeth standing side by side on green"></div>

    <section class="services">
      <article class="service">
        <svg class="service-icon" viewBox="0 0 44 50" fill="none" stroke="#c6de3a" stroke-width="2.5" stroke-linejoin="round">
          <path d="M8 10c4-6 10-4 14-2 4-2 10-4 14 2 3 6 0 12-2 18l-3 16c-1 3-4 3-4 0l-2-12h-6l-2 12c0 3-3 3-4 0l-3-16C8 22 5 16 8 10z"/>
          <path d="M36 2l2 5 5 2-5 2-2 5-2-5-5-2 5-2z" stroke-width="2"/>
        </svg>
        <h2 class="service-title">Cosmetic Dentistry</h2>
        <p class="service-text">Whitening, veneers, and smile makeovers for a confident appearance.</p>
      </article>
      <article class="service">
        <svg class="service-icon" viewBox="0 0 44 50" fill="none" stroke="#c6de3a" stroke-width="2.5" stroke-linejoin="round">
          <path d="M12 4c4-3 8-1 10 0 2-1 6-3 10 0 3 3 2 9 0 12H12c-2-3-3-9 0-12z"/>
          <path d="M14 20h16M15 26h14M16 32h12M17 38h10M19 44h6"/>
        </svg>
        <h2 class="service-title">Dental Implants</h2>
        <p class="service-text">Permanent tooth replacement with natural look, feel, and function.</p>
      </article>
      <article class="service">
        <svg class="service-icon" viewBox="0 0 44 50" fill="none" stroke="#c6de3a" stroke-width="2.5" stroke-linecap="round" stroke-linejoin="round">
          <path d="M6 44l24-24"/>
          <path d="M24 18l6 6 5-5-6-6z"/>
          <path d="M36 4c3 4 4 6 4 8a4 4 0 0 1-8 0c0-2 1-4 4-8z"/>
        </svg>
        <h2 class="service-title">Hygiene &amp; Cleanings</h2>
        <p class="service-text">Thorough, professional cleanings to protect your oral health.</p>
      </article>
      <article class="service">
        <svg class="service-icon" viewBox="0 0 44 50" fill="none" stroke="#c6de3a" stroke-width="2.5" stroke-linejoin="round">
          <path d="M22 3l16 6v14c0 11-7 19-16 24C13 42 6 34 6 23V9z"/>
          <path d="M18 17h8v5h5v8h-5v5h-8v-5h-5v-8h5z"/>
        </svg>
        <h2 class="service-title">Emergency Services</h2>
        <p class="service-text">Prompt, compassionate care when dental issues can't wait.</p>
      </article>
      <article class="service">
        <svg class="service-icon" viewBox="0 0 44 50" fill="none" stroke="#c6de3a" stroke-width="2.5" stroke-linejoin="round">
          <path d="M10 6l6 5 6-7 6 7 6-5 2 14H8z"/>
          <path d="M8 20c0 6 1 10 3 14l2 12c1 2 3 2 4 0l2-12h6l2 12c1 2 3 2 4 0l2-12c2-4 3-8 3-14"/>
        </svg>
        <h2 class="service-title">Restorations</h2>
        <p class="service-text">Repair and strengthen teeth with expertly crafted solutions.</p>
      </article>
      <article class="service">
        <svg class="service-icon" viewBox="0 0 44 50" fill="none" stroke="#c6de3a" stroke-width="2.5" stroke-linejoin="round">
          <path d="M3 16c10-8 28-8 38 0"/>
          <path d="M4 18c0 10 8 16 18 16s18-6 18-16"/>
          <path d="M9 22v6M15 24v8M22 25v9M29 24v8M35 22v6"/>
        </svg>
        <h2 class="service-title">Dentures &amp; Partials</h2>
        <p class="service-text">Custom full or partial dentures designed for comfort and fit.</p>
      </article>
    </section>

    <div class="web">MEADOWFIELDDENTISTRYTN.COM</div>
  </main>
</body>
</html>
```